I want ideas sample designs for my book cover

Hello,

We need a book cover designed in flat and 3D Versions. We would like to have jpg and png for final output and include a copy of the PSD for future revisions.

Here are the basic details:

Title: The Harvest Lantern Keepers
Author: Dominic Harwell

Dimensions of book:

Was looking at the Pexo website for dimensions. I thought you may want to go on there and look at the different sizes. I used the 6x9” perfect bound US trade size for my book. You will see that this has a spine width of 0.225”, Cover size of 12.48 x 9.25” and spine begins at 6.125”

If you need background info on the author just to get an idea what he does, please check:

http://DominicHarwell.example

IMPORTANT: Please see attached document for a more detailed info:

Exact Title Of book
Back Cover
Spine Info
Measurements of book and dimension
Examples of book covers
Dominic's photo attached

Thanks,
Rosalind

Industry/Entity Type

Life Coaching

Font styles to use
Serif

Requirements
Must have
• Jpg, png and PSD files
• title
• author
• exact dimensions
• front and back cover
• flat and 3d versions

```html
<!DOCTYPE html>
<html lang="en">
<head>
<meta charset="utf-8">
<title>The Harvest Lantern Keepers — Cover Wrap</title>
<link rel="stylesheet" href="https://fonts.googleapis.com/css2?family=Source+Serif+4:wght@400;600;700&display=swap">
<style>
  :root {
    --page-bg: #ffffff;
    --navy: #1d3d68;
    --band-white: #f7f8fa;
    --slate: #7f9cb4;
    --slate-dark: #6f8ca4;
    --ink: #1f3049;
    --name-box: #dde6ee;
    --floor: #c9ced3;
    --serif: "Source Serif 4", Georgia, serif;
  }
  * { box-sizing: border-box; margin: 0; padding: 0; }
  html, body {
    width: 1200px; height: 850px; overflow: hidden;
    background: var(--page-bg);
  }
  .cover-wrap {
    position: absolute; left: 95px; top: 65px;
    width: 1010px; height: 720px;
    display: flex;
    box-shadow: 0 6px 24px rgba(0,0,0,0.18);
  }

  /* Back cover */
  .back-cover {
    position: relative; width: 490px; height: 100%;
    background: linear-gradient(180deg, #86a2b9 0%, var(--slate) 60%, #7794ac 100%);
    color: var(--ink);
  }
  .back-band {
    position: absolute; left: 25px; top: 0; width: 50px; height: 100%;
    background: var(--navy);
  }
  .back-website {
    position: absolute; left: 25px; top: 20px; width: 50px; height: 220px;
    display: flex; align-items: center; justify-content: center;
  }
  .back-website span {
    display: block; transform: rotate(-90deg); white-space: nowrap;
    font-family: var(--serif); font-size: 15px; letter-spacing: 0.3px;
    color: #e8eef4;
  }
  .back-author {
    position: absolute; left: 25px; top: 255px; width: 118px; height: 74px;
    background: var(--name-box);
    padding: 9px 8px;
    font-family: var(--serif); font-weight: 700; font-size: 21px; line-height: 27px;
    color: var(--navy); white-space: nowrap;
  }
  .author-photo {
    position: absolute; left: 25px; top: 345px; width: 118px; height: 240px;
    background: linear-gradient(180deg, #5a6470 0%, #9ca4ac 55%, #e4e6e8 100%);
  }
  .back-copy {
    position: absolute; left: 160px; top: 26px; width: 305px;
    font-family: var(--serif); font-size: 8.6px; line-height: 12px;
    text-align: justify;
  }
  .back-copy p + p { margin-top: 12px; }

  /* Spine */
  .spine {
    position: relative; width: 30px; height: 100%;
    background: var(--slate-dark);
    display: flex; align-items: center; justify-content: center;
  }
  .spine-title {
    transform: rotate(90deg); white-space: nowrap;
    font-family: var(--serif); font-size: 16px; letter-spacing: 0.5px;
    text-transform: uppercase; color: var(--ink);
  }

  /* Front cover */
  .front-cover {
    position: relative; width: 490px; height: 100%; overflow: hidden;
  }
  .front-artwork {
    position: absolute; inset: 0;
    background: linear-gradient(180deg, #3c5f88 0%, #52779e 35%, #8fa7bf 70%, var(--floor) 86%, #dfe2e5 100%);
  }
  .title-band {
    position: absolute; left: 0; top: 190px; width: 100%; height: 190px;
    background: var(--band-white);
  }
  .book-title {
    position: absolute; left: 10px; right: 140px; top: 208px;
    text-align: right; white-space: nowrap;
    font-family: var(--serif); font-weight: 600; font-size: 44px; line-height: 52px;
    text-transform: uppercase; color: var(--navy);
  }
  .subtitle-band {
    position: absolute; left: 0; top: 386px; width: 100%; height: 86px;
    background: var(--navy);
  }
  .subtitle {
    position: absolute; left: 20px; right: 140px; top: 400px;
    text-align: right;
    font-family: var(--serif); font-size: 13px; line-height: 18px;
    color: #f2f5f8;
  }
  .author-band {
    position: absolute; left: 0; top: 478px; width: 100%; height: 130px;
    background: var(--band-white);
  }
  .author-credit {
    position: absolute; left: 10px; right: 140px; top: 506px; text-align: right;
    font-family: var(--serif); color: var(--navy); text-transform: uppercase;
    white-space: nowrap;
  }
  .author-credit .credit-line { font-size: 13px; line-height: 20px; font-weight: 600; letter-spacing: 0.2px; }
  .author-credit .author-name { font-size: 34px; line-height: 46px; font-weight: 600; }
</style>
</head>
<body>
  <div class="cover-wrap">
    <section class="back-cover">
      <div class="back-band"></div>
      <div class="back-website"><span>www.DominicHarwell.example</span></div>
      <div class="back-author">DOMINIC<br>HARWELL</div>
      <div class="author-photo" role="img" aria-label="Black and white portrait photo of the author"></div>
      <div class="back-copy">
        <p>This path goes far beyond business. This is a book for the awakening entrepreneurs who are building companies for a better world, shaping generations to come. Bringing you gently disruptive ideas, it will turn you and your business inside-out for real growth towards your vision, mission and values.</p>
        <p>There is the potential to live a more meaningful life and run a kinder business by discovering the quiet bonds that connect all beings. You will be invited to take your life and work to the next level as you answer the call within these pages, building honest ties with yourself, your partner, your family, your friends, your colleagues and Mother Earth.</p>
        <p>A lantern keeper is one who tends a small flame through the long night so that others may find their way home. The practice is old, patient and simple, and it is helping founders, leaders and makers to lead with clarity, release fear and build success that lasts both personally and professionally.</p>
        <p>Dominic shares his own heartfelt stories and lessons gathered from years of travel, teaching and listening. He believes that if enough people explore their own inner light, together we can make a lasting difference. If you are ready to take the journey within, you will find the missing link you have been searching for.</p>
        <p>Dominic Harwell is a speaker, coach, mentor and best-selling author who has spoken to audiences in many countries. In his second book he challenges you to examine the core of your true nature and how it shapes your journey. Dominic's gift is to join purpose with profit in a way that brings deeper meaning to the work we are here to do.</p>
      </div>
    </section>

    <section class="spine">
      <div class="spine-title">The Harvest Lantern Keepers</div>
    </section>

    <section class="front-cover">
      <div class="front-artwork" role="img" aria-label="Photo of a businesswoman with a briefcase standing before a blue chalkboard covered in sketched business diagrams and icons"></div>
      <div class="title-band"></div>
      <h1 class="book-title">The Harvest<br>Lantern<br>Keepers</h1>
      <div class="subtitle-band"></div>
      <p class="subtitle">How this ancient wisdom is helping billionaires, industry icons and entrepreneurs to be better leaders, increase impact and leave a legacy.</p>
      <div class="author-band"></div>
      <div class="author-credit">
        <div class="credit-line">From the best selling author of “Awaken”</div>
        <div class="author-name">Dominic Harwell</div>
      </div>
    </section>
  </div>
</body>
</html>
```